WWW.VELTRONA.IT BUSINNES CARD

WE NEED A BUSINESS CARD . I HAVE A COMPANY IN ITALY NR 1 IN HAIR MEDICAL CARE AN HAIR REPLECEMENT . IN CARD I NEED WRITE WEB ADDRESS, MAIL , ADDRESS, TELEPHONE NUMBER , AND NAME
IN THE BACK SIDE I NEED MY DOCTOR LOGO .
MY WEB SITE IS WWW.VELTRONA.IT
Updates

Target Market(s)

CONSUMER B2C

Industry/Entity Type

Hair And Beauty

Contact Information for Business Card

I WANT A MEDICAL BUSINESS CARD.

Font styles to use
Other font styles liked:
• VERDANA

Colors
33a6d7
3176b5
85abd2
aedbee
eaf1f7
ffffff

Requirements
Must have
• I NEED MY LOGO AND LOGO OF DR VELTRONA

```html
<!DOCTYPE html>
<html lang="en">
<head>
<meta charset="utf-8">
<title>Veltrona Business Card</title>
<link rel="stylesheet" href="https://fonts.googleapis.com/css2?family=Noto+Sans:wght@400;700&display=swap">
<style>
  :root {
    --backdrop: #7b7b7b;
    --paper: #f4f4f2;
    --brand-navy: #1c4f9c;
    --brand-sky: #2eafe2;
    --brand-deep: #24468f;
    --ink: #222222;
    --white: #ffffff;
    --figure-brown: #6b3a1f;
    --figure-tan: #e9a987;
  }
  * { margin: 0; padding: 0; box-sizing: border-box; }
  html, body {
    width: 1200px; height: 982px; overflow: hidden;
    background: var(--backdrop);
    font-family: "Noto Sans", Verdana, sans-serif;
  }
  .stage {
    position: relative; width: 1200px; height: 982px;
    display: flex; justify-content: center; align-items: center; gap: 70px;
  }
  .card {
    position: relative; width: 360px; height: 590px;
    background: var(--paper); overflow: hidden;
    box-shadow: 0 6px 14px rgba(0,0,0,.28);
  }
  .card-wave { position: absolute; left: 0; bottom: 0; width: 360px; height: 170px; display: block; }

  /* front */
  .brand { position: absolute; top: 88px; left: 0; width: 100%; text-align: center; }
  .brand-row { display: inline-flex; align-items: center; gap: 12px; }
  .brand-mark { width: 30px; height: 30px; background: var(--brand-sky); border-radius: 4px; }
  .brand-name { font-size: 42px; font-weight: 700; color: var(--brand-navy); letter-spacing: .5px; line-height: 1; }
  .brand-tagline { margin-top: 8px; font-size: 12px; color: var(--brand-sky); letter-spacing: .4px; }
  .brand-swoosh { position: absolute; top: 172px; left: 40px; width: 290px; height: 40px; display: block; }

  .person { position: absolute; top: 280px; width: 100%; text-align: center; }
  .person-name { font-size: 26px; font-weight: 700; color: var(--brand-navy); letter-spacing: 1px; line-height: 1.1; }
  .person-role { font-size: 13px; color: var(--ink); letter-spacing: .6px; }

  .contact { position: absolute; top: 360px; width: 100%; text-align: center; color: var(--ink); font-size: 14px; letter-spacing: 1px; line-height: 1.3; }
  .contact-icon { display: block; margin: 0 auto 4px; }
  .contact-item + .contact-item { margin-top: 10px; }

  .card-url {
    position: absolute; bottom: 50px; width: 100%; text-align: center;
    color: var(--white); font-size: 15px; letter-spacing: 1.6px;
  }
  .card-back .card-url { bottom: 62px; }

  /* back */
  .mascot-area {
    position: absolute; top: 80px; left: 80px; width: 170px; height: 330px;
    border-radius: 80px 80px 50% 50% / 60px 60px 40px 40px;
    background: linear-gradient(180deg, var(--figure-brown) 0%, #8a5634 55%, var(--figure-tan) 100%);
    opacity: .85;
  }
  .doctor-name {
    position: absolute; top: 360px; left: 268px;
    transform: rotate(-90deg); transform-origin: left top;
    font-size: 22px; font-weight: 700; color: var(--brand-navy); white-space: nowrap;
  }
</style>
</head>
<body>
<main class="stage">

  <section class="card card-front" aria-label="Business card front">
    <div class="brand">
      <div class="brand-row">
        <span class="brand-mark"></span>
        <span class="brand-name">Veltrona</span>
      </div>
      <p class="brand-tagline">CURA E REINTEGRAZIONE DEI CAPELLI</p>
    </div>
    <svg class="brand-swoosh" viewBox="0 0 290 40" aria-hidden="true">
      <path d="M2 36 C 90 12, 200 28, 288 2" fill="none" stroke="#2eafe2" stroke-width="2.5" stroke-linecap="round"/>
    </svg>

    <div class="person">
      <p class="person-name">Marco Bellini</p>
      <p class="person-role">Founder &amp; CEO</p>
    </div>

    <div class="contact">
      <div class="contact-item">
        <svg class="contact-icon" width="18" height="18" viewBox="0 0 24 24" aria-hidden="true">
          <path fill="#1c4f9c" d="M6.6 10.8a15.1 15.1 0 0 0 6.6 6.6l2.2-2.2a1 1 0 0 1 1-.25 11.4 11.4 0 0 0 3.6.57 1 1 0 0 1 1 1V20a1 1 0 0 1-1 1A17 17 0 0 1 3 4a1 1 0 0 1 1-1h3.5a1 1 0 0 1 1 1c0 1.25.2 2.45.57 3.6a1 1 0 0 1-.25 1z"/>
        </svg>
        123 555 0190
      </div>
      <div class="contact-item">
        <svg class="contact-icon" width="22" height="16" viewBox="0 0 22 16" aria-hidden="true">
          <rect x="0" y="0" width="22" height="16" rx="1.5" fill="#1c4f9c"/>
          <path d="M1 1.5 11 9l10-7.5" fill="none" stroke="#f4f4f2" stroke-width="1.6"/>
        </svg>
        marco@veltrona.com.au
      </div>
    </div>

    <svg class="card-wave" viewBox="0 0 360 170" preserveAspectRatio="none" aria-hidden="true">
      <path fill="#2eafe2" d="M0 92 C 70 55, 150 60, 230 68 S 330 60, 360 22 L 360 170 L 0 170 Z"/>
    </svg>
    <p class="card-url">www.veltrona.com.au</p>
  </section>

  <section class="card card-back" aria-label="Business card back">
    <div class="mascot-area" role="img" aria-label="Cartoon doctor mascot illustration"></div>
    <p class="doctor-name">dr. Veltrona</p>

    <svg class="card-wave" viewBox="0 0 360 170" preserveAspectRatio="none" aria-hidden="true">
      <path fill="#24468f" d="M0 95 C 60 60, 140 60, 210 50 S 320 20, 360 0 L 360 170 L 0 170 Z"/>
    </svg>
    <p class="card-url">www.veltrona.com.au</p>
  </section>

</main>
</body>
</html>
```